Billboard for a Contractor in Minnesota

Creating our first billboard that will be displayed on a freeway. Will be used on a digital Flick Signboard. Sign should be a 846 x 234 design. Our website is tamber-paving.com Looking for something specific to "Look us up" or "Call" for your free concrete & asphalt estimate. Needs both web addresses (tamber-paving.com and tamber-masonry.com. Needs our phone number, logo. Our slogan is Serving All Your Asphalt & Concrete Needs. It's also our 25 Anniversary.

Target Market(s)

Residential Homeowners in the Twin Cities

Colors
abd036

Requirements
Must have
• Logo, Phone Number, Our Services, Web Addresses (both) Our services are all on our website. (Asphalt Driveway, Concrete Driveway, Concrete Apron, Concrete Sidewalk, Concrete Patio. Colors should be same as website. Black, White, Gray and the Neon Green color.

```html
<!DOCTYPE html>
<html lang="en">
<head>
<meta charset="utf-8">
<title>Tamber Paving – Billboard</title>
<link href="https://fonts.googleapis.com/css2?family=Fira+Sans:wght@400;600;700;800&display=swap" rel="stylesheet">
<style>
  :root {
    --green: #2aa317;
    --green-light: #6fcb4a;
    --neon: #abd036;
    --black: #0b0b0b;
    --white: #ffffff;
    --gray: #3a3a3a;
    --badge: #1b5f7f;
    --page: #eceeef;
  }
  * { margin: 0; padding: 0; box-sizing: border-box; }
  html, body { width: 1156px; height: 1200px; overflow: hidden; background: var(--page); }
  body { position: relative; font-family: "Fira Sans", sans-serif; }

  .billboard-wrap {
    position: absolute; left: 28px; top: 448px;
    width: 1100px; height: 304px;
    box-shadow: 0 6px 18px rgba(0,0,0,.18);
  }
  .billboard {
    position: absolute; left: 0; top: 0;
    width: 1180px; height: 326px;
    transform: scale(0.9322); transform-origin: 0 0;
    overflow: hidden; background: var(--white);
  }

  .hero-scene {
    position: absolute; left: 0; top: 0; width: 1180px; height: 258px;
    background: linear-gradient(180deg, #b9e2f4 0%, #d9edf5 45%, #e6ebea 58%, #cfc8b6 72%, #d9c89a 100%);
  }
  .hero-road {
    position: absolute; left: 0; top: 0; width: 1180px; height: 258px;
    background: radial-gradient(ellipse 260px 110px at 590px 270px, rgba(40,35,40,.55), rgba(40,35,40,0) 100%);
  }

  .brand {
    position: absolute; left: 30px; top: 88px; width: 320px;
    text-align: center; color: var(--black); font-weight: 800;
  }
  .brand-name { font-size: 74px; letter-spacing: 6px; line-height: 1; }
  .brand-sub { font-size: 22px; letter-spacing: 1.5px; margin-top: 18px; line-height: 1; }
  .brand-rule { position: absolute; left: 36px; top: 218px; width: 288px; height: 8px; background: var(--black); }

  .headline {
    position: absolute; left: 320px; top: 36px; width: 560px;
    text-align: center; font-weight: 700; font-size: 35px; line-height: 40px;
    color: #151515; letter-spacing: .3px;
  }
  .estimate-cta {
    position: absolute; left: 320px; top: 128px; width: 560px;
    text-align: center; font-weight: 700; font-size: 21px; line-height: 26px; color: #151515;
  }
  .estimate-cta strong { color: var(--green); }
  .anniversary {
    position: absolute; left: 505px; top: 166px; width: 190px; height: 30px;
    background: var(--black); color: var(--neon); border-radius: 15px;
    text-align: center; font-weight: 700; font-size: 16px; line-height: 30px; letter-spacing: 1px;
  }

  .services-back {
    position: absolute; left: 895px; top: 18px; width: 268px; height: 232px;
    background: var(--green-light); border-radius: 16px; transform: rotate(4deg);
  }
  .services {
    position: absolute; left: 896px; top: 32px; width: 250px; height: 210px;
    background: var(--green); border-radius: 14px; transform: rotate(-1.5deg);
    padding: 12px 0 0 16px; list-style: none;
  }
  .services li {
    display: flex; align-items: center; gap: 10px;
    color: var(--white); font-weight: 700; font-size: 19px; height: 36.5px;
  }
  .services svg { width: 17px; height: 17px; flex: none; }

  .footer-bar { position: absolute; left: 0; top: 258px; width: 1180px; height: 68px; }
  .websites {
    position: absolute; left: 45px; top: 262px;
    font-size: 26px; color: var(--gray); font-weight: 400; line-height: 30px;
  }
  .websites strong { color: var(--green); font-weight: 700; }
  .rating-badge {
    position: absolute; left: 530px; top: 275px; width: 70px; height: 38px;
    background: var(--badge); border: 2px solid #c9d6dc;
  }
  .call-label {
    position: absolute; left: 688px; top: 287px;
    color: var(--green); font-weight: 700; font-size: 18px; letter-spacing: .3px;
  }
  .phone {
    position: absolute; left: 850px; top: 268px;
    color: var(--white); font-weight: 700; font-size: 46px; line-height: 54px; letter-spacing: .5px;
  }
</style>
</head>
<body>
  <div class="billboard-wrap">
    <div class="billboard">
      <div class="hero-scene" role="img" aria-label="Photo of a straight asphalt highway stretching to the horizon through pale fields under a light blue sky"></div>
      <div class="hero-road" aria-hidden="true"></div>

      <div class="brand">
        <div class="brand-name">TAMBER</div>
        <div class="brand-sub">PAVING &amp; MASONRY</div>
      </div>
      <div class="brand-rule"></div>

      <h1 class="headline">SERVING ALL YOUR ASPHALT<br>&amp; CONCRETE NEEDS</h1>
      <p class="estimate-cta">Call or look us up for your <strong>FREE estimate!</strong></p>
      <div class="anniversary">25 YEARS STRONG</div>

      <div class="services-back"></div>
      <ul class="services">
        <li><svg viewBox="0 0 20 20"><circle cx="10" cy="10" r="8" fill="none" stroke="#fff" stroke-width="1.6"/><path d="M6 10.3l2.7 2.7L14.5 7" fill="none" stroke="#fff" stroke-width="1.8" stroke-linecap="round" stroke-linejoin="round"/></svg>Asphalt Driveway</li>
        <li><svg viewBox="0 0 20 20"><circle cx="10" cy="10" r="8" fill="none" stroke="#fff" stroke-width="1.6"/><path d="M6 10.3l2.7 2.7L14.5 7" fill="none" stroke="#fff" stroke-width="1.8" stroke-linecap="round" stroke-linejoin="round"/></svg>Concrete Driveway</li>
        <li><svg viewBox="0 0 20 20"><circle cx="10" cy="10" r="8" fill="none" stroke="#fff" stroke-width="1.6"/><path d="M6 10.3l2.7 2.7L14.5 7" fill="none" stroke="#fff" stroke-width="1.8" stroke-linecap="round" stroke-linejoin="round"/></svg>Concrete Apron</li>
        <li><svg viewBox="0 0 20 20"><circle cx="10" cy="10" r="8" fill="none" stroke="#fff" stroke-width="1.6"/><path d="M6 10.3l2.7 2.7L14.5 7" fill="none" stroke="#fff" stroke-width="1.8" stroke-linecap="round" stroke-linejoin="round"/></svg>Concrete Sidewalk</li>
        <li><svg viewBox="0 0 20 20"><circle cx="10" cy="10" r="8" fill="none" stroke="#fff" stroke-width="1.6"/><path d="M6 10.3l2.7 2.7L14.5 7" fill="none" stroke="#fff" stroke-width="1.8" stroke-linecap="round" stroke-linejoin="round"/></svg>Concrete Patio</li>
      </ul>

      <svg class="footer-bar" viewBox="0 0 1180 68" aria-hidden="true">
        <rect x="0" y="0" width="1180" height="68" fill="#fff"/>
        <polygon points="648,0 668,0 640,68 620,68" fill="#2aa317"/>
        <polygon points="668,0 1180,0 1180,68 640,68" fill="#0b0b0b"/>
      </svg>
      <div class="websites">
        <div>www.<strong>tamber-paving</strong>.com</div>
        <div>www.<strong>tamber-masonry</strong>.com</div>
      </div>
      <div class="rating-badge"></div>
      <div class="call-label">CALL US TODAY!</div>
      <div class="phone">612-555-0148</div>
    </div>
  </div>
</body>
</html>
```